Ironbell Lounge

We are a small Bar & Bistro that specializes in Napolitano and Artisan pizzas. We have a full bar with an emphasis on craft cocktails, scotch, bourbon and whisk(e)y. Our theme and decor is a reflection of a Speakeasy or Prohibition Era. This postcard is to be used to market and promote our "Late Night Happy Hour." Our cocktail list includes Prohibition libations such as the Sazerac, Vesper, Old Fashion and the Sidecar.

Photos 1-4 are our logo, pizza oven and interior photos. I don't need both interior photos, only one will be fine. But the logo and pizza oven photo are a must. I also need to showcase the fact that we are pouring cocktails. Not so much beer and wine, but would like to see a Manhattan or an Old Fashion photo up there.

The other photos are just stock photos I pulled from the internet that I felt best describes the feel of our restaurant/bar. I want this to have a dark, masculine, 1920's, vintage, speakeasy, prohibition, sexy, sultry, blues, exclusive feel. I want to attract the late night crowd, and the service industry people as well. I was thinking of adding, "Where the Hospitality Industry Professionals get waited on"

We have a Baby Grand Piano as well, so live music is a big thing for us attracting our late night crowd.

Target Market(s)

Hospitality Industry & 30 year old +

Industry/Entity Type

Internet

Requirements
Must have
• Heading/Title to read:

Ember Table & Tavern
A Hideaway for the Ironbell Regulars

Somewhere among everything I need it to read...(but doesn't have to be all together)..

Late Night Happy Hour Friday & Saturday
Live Blues Music 10pm - Midnight
$5 cocktails
$5 drafts
$5 wine by the glass
Napolitano and Artisan Pizza's
Nice to have
• Colors: I would like to see are black, copper, mahogany, rich browns, sepia tones, maybe even some golds. I am definitely open though on any creative ideas that are eye catching and go along with the theme.

```html
<!DOCTYPE html>
<html lang="en">
<head>
<meta charset="utf-8">
<title>Ember Table &amp; Tavern – Late Night Happy Hour Postcard</title>
<link rel="stylesheet" href="https://fonts.googleapis.com/css2?family=Merriweather:wght@400;700&family=Oswald:wght@400&display=swap">
<style>
  :root {
    --navy: #0b0f5c;
    --cream: #fff4c4;
    --panel: #222122;
    --panel-edge: #5c5548;
    --rust: #a3412a;
    --white: #ffffff;
    --ink: #2a2a2a;
    --card-edge: #555555;
    --amber: #e8a24a;
    --ember: #f28a1c;
  }
  * { margin: 0; padding: 0; box-sizing: border-box; }
  html, body { width: 738px; height: 1200px; overflow: hidden; background: var(--white); }
  body { position: relative; font-family: "Merriweather", Georgia, serif; }

  .front {
    position: absolute; left: 0; top: 0; width: 736px; height: 566px; overflow: hidden;
    background:
      repeating-linear-gradient(180deg, rgba(196,150,70,0.18) 0px, rgba(120,80,110,0.10) 7px, rgba(196,150,70,0.14) 13px, rgba(90,60,100,0.12) 19px),
      linear-gradient(180deg, #6a4a70 0%, #7e6447 20%, #95733c 34%, #6f5169 52%, #92703f 70%, #7a5e4a 84%, #694a6e 100%);
  }
  .title-band {
    position: absolute; left: 0; top: 0; width: 736px; height: 51px;
    background: var(--navy); border-bottom: 2px solid #9c8f74;
  }
  .title-band h1 {
    position: absolute; left: 194px; top: 8px;
    font-size: 27px; font-weight: 700; color: var(--cream); white-space: nowrap;
  }

  .brand-plate {
    position: absolute; left: 18px; top: 7px; width: 158px; height: 158px;
    background: var(--white); border: 2px solid #b7a27a; border-radius: 6px; z-index: 2;
    text-align: center; padding-top: 36px;
  }
  .brand-name { font-size: 19px; font-weight: 700; color: var(--rust); line-height: 1.2; }
  .brand-contact { margin-top: 12px; font-size: 9.5px; color: var(--ink); line-height: 1.45; }

  .side-column {
    position: absolute; left: 29px; top: 156px; width: 127px; height: 393px;
    background: var(--panel); border: 1px solid var(--panel-edge);
  }
  .side-text {
    position: absolute; left: 0; width: 127px; text-align: center;
    color: var(--white); font-weight: 700; font-size: 13.5px; line-height: 17.5px;
  }
  .side-text.live { font-size: 17px; text-decoration: underline; }
  .divider {
    position: absolute; left: 36px; width: 56px; height: 22px;
    background: radial-gradient(ellipse at 50% 50%, #d9d3a0 0%, #8d8a5a 30%, #2c2b22 75%, #1c1c1a 100%);
  }

  .photo { position: absolute; border: 2px solid #4a4436; }
  .bar-interior {
    left: 182px; top: 67px; width: 384px; height: 255px;
    background:
      radial-gradient(circle at 30% 18%, rgba(255,226,160,0.85) 0, rgba(255,200,120,0.25) 18px, transparent 34px),
      radial-gradient(circle at 18% 26%, rgba(255,226,160,0.7) 0, rgba(255,200,120,0.2) 14px, transparent 28px),
      radial-gradient(circle at 58% 40%, rgba(255,190,110,0.55) 0, transparent 60px),
      radial-gradient(ellipse 190px 60px at 66% 80%, rgba(236,226,205,0.9) 0, rgba(210,190,160,0.5) 50%, transparent 100%),
      radial-gradient(ellipse 120px 70px at 88% 15%, rgba(244,214,160,0.55) 0, transparent 100%),
      linear-gradient(180deg, #2a1e16 0%, #6e4122 28%, #a2642e 45%, #5a3a22 62%, #3a2a1c 82%, #1f1611 100%);
  }

  .pizza-panel { position: absolute; left: 182px; top: 340px; width: 261px; height: 205px;
    background: var(--panel); border: 1px solid var(--panel-edge); }
  .pizza-panel h2 { font-size: 14.5px; font-weight: 700; color: var(--white); padding: 5px 0 0 10px; white-space: nowrap; }
  .oven {
    left: 5px; top: 33px; width: 251px; height: 168px; border: none;
    background:
      radial-gradient(ellipse 110px 70px at 52% 42%, #ffe08a 0%, #ffb437 35%, transparent 100%),
      radial-gradient(ellipse 150px 95px at 48% 55%, var(--ember) 0%, #c4480f 55%, transparent 100%),
      radial-gradient(ellipse 90px 30px at 25% 88%, rgba(255,160,60,0.8) 0%, transparent 100%),
      linear-gradient(180deg, #3a1206 0%, #6b1e08 40%, #8a3a10 80%, #2a0d05 100%);
  }

  .quote-panel { position: absolute; left: 460px; top: 340px; width: 108px; height: 205px;
    background: var(--panel); border: 1px solid var(--panel-edge);
    font-family: "Oswald", "Arial Narrow", sans-serif; color: var(--white);
    font-size: 18.5px; line-height: 26.5px; text-align: center; padding-top: 8px; }

  .right-column { position: absolute; left: 587px; top: 67px; width: 132px; height: 480px;
    background: var(--panel); border: 1px solid var(--panel-edge); }
  .martini {
    left: 28px; top: 7px; width: 75px; height: 75px; border: none;
    background:
      radial-gradient(ellipse 26px 16px at 50% 38%, #c55a62 0%, #8e3a44 60%, transparent 100%),
      linear-gradient(180deg, #f2f2f2 0%, #cfcfd2 30%, #6a5a5e 70%, #1d1d1d 100%);
  }
  .old-fashioned {
    left: 30px; top: 119px; width: 72px; height: 71px; border: none;
    background:
      radial-gradient(ellipse 26px 30px at 50% 55%, #e08a2a 0%, #a4501a 55%, transparent 100%),
      linear-gradient(180deg, #1c140f 0%, #4a2a16 50%, #2a1a10 85%, #d9d3cc 100%);
  }
  .piano {
    left: 10px; top: 250px; width: 111px; height: 73px; border: none;
    background:
      linear-gradient(165deg, #1a1a1a 0%, #444 30%, #b8b8b8 55%, #f4f4f4 80%, #dcdcdc 100%);
  }
  .saxophone {
    left: 7px; top: 386px; width: 118px; height: 74px; border: none;
    background:
      radial-gradient(ellipse 40px 30px at 55% 35%, #ffd27a 0%, #e09a32 45%, transparent 100%),
      radial-gradient(ellipse 80px 55px at 50% 45%, #b26c1c 0%, #5a3410 65%, #1e1208 100%);
  }
  .right-column .divider { left: 37px; top: 203px; width: 58px; height: 30px; }
  .right-label { position: absolute; left: 0; width: 130px; text-align: center;
    color: var(--white); font-weight: 700; font-size: 17px; line-height: 21px; }

  .back {
    position: absolute; left: 1px; top: 634px; width: 736px; height: 564px;
    border: 1px solid var(--card-edge); background: var(--white);
  }
  .back .brand-plate { left: 48px; top: 43px; width: 180px; height: 200px; padding-top: 50px; }
  .back .brand-name { font-size: 21px; }
  .back .brand-contact { font-size: 10.5px; margin-top: 14px; }
</style>
</head>
<body>

<section class="front">
  <header class="title-band">
    <h1>A Hideaway for the Ironbell Regulars</h1>
  </header>

  <div class="brand-plate">
    <p class="brand-name">Ember Table<br>&amp; Tavern</p>
    <p class="brand-contact">418 Cedar Row<br>Harbor Point<br>555.014.2290</p>
  </div>

  <aside class="side-column">
    <p class="side-text" style="top:52px">Late Night<br>Happy Hour<br>Fridays &amp;<br>Saturdays</p>
    <div class="divider" style="top:127px" role="img" aria-label="Small scroll divider ornament"></div>
    <p class="side-text live" style="top:157px">LIVE</p>
    <p class="side-text" style="top:178px">Blues Music<br>10pm to<br>Midnight</p>
    <div class="divider" style="top:240px" role="img" aria-label="Small scroll divider ornament"></div>
    <p class="side-text" style="top:273px">$5 cocktails<br>$5 drafts<br>$5 wine by<br>the glass</p>
    <div class="divider" style="top:359px" role="img" aria-label="Small scroll divider ornament"></div>
  </aside>

  <div class="photo bar-interior" role="img" aria-label="Photo of the lounge interior with a long marble bar, pendant lights and guests at tables"></div>

  <div class="pizza-panel">
    <h2>Neapolitan and Artisan Pizza's</h2>
    <div class="photo oven" role="img" aria-label="Photo of flames inside the wood-fired pizza oven"></div>
  </div>

  <blockquote class="quote-panel">“Where<br>Hospitality<br>Industry<br>Professionals<br>are<br>waited<br>on.”</blockquote>

  <aside class="right-column">
    <div class="photo martini" role="img" aria-label="Photo of a pink cocktail in a martini glass"></div>
    <p class="right-label" style="top:93px">cocktails</p>
    <div class="photo old-fashioned" role="img" aria-label="Photo of an old fashioned cocktail with ice and orange peel"></div>
    <div class="divider" role="img" aria-label="Small scroll divider ornament"></div>
    <div class="photo piano" role="img" aria-label="Black and white photo of grand piano keys"></div>
    <p class="right-label" style="top:332px">grand piano<br>&amp; the blues</p>
    <div class="photo saxophone" role="img" aria-label="Silhouette of a saxophone player against warm golden light"></div>
  </aside>
</section>

<section class="back">
  <div class="brand-plate">
    <p class="brand-name">Ember Table<br>&amp; Tavern</p>
    <p class="brand-contact">418 Cedar Row<br>Harbor Point<br>555.014.2290</p>
  </div>
</section>

</body>
</html>
```